Wordpress Design - Accounting Practice Startup

We are a relatively new Accounting Firm in Sydney with a primary focus on the Not-For-Profit sector. We need a complete re-design of our wordpress based website: www.tallowmereledger.com.au
We already have a logo design which we would like to keep using. See uploaded files.
We have a simple menu stucture:
- Home
- About Us
- Our Services
- Contact Us
(Suggestions welcome!)
Happy for it to be a single page scrolling website linked via the menu. We would like the "Our Services" page/section to have icons for the following:
- Bookkeeping
- Payroll
- Accounting
- Training
- Consulting
- Projects
We'd like a banner at the top of the page below the menu, and a place for testimonials, possibly integrated into the body or to the side. Images and icons to be included would be great.
Our main aim is to have an elegant and modern website that works well on all devices.
Updates
Industry/Entity Type
Accounting
Colors
Designer to choose colors to be used in the design.
Look and feel
Each slider illustrates characteristics of the customer's brand and the style your logo design should communicate.

```html
<!DOCTYPE html>
<html lang="en">
<head>
<meta charset="utf-8">
<title>About Us – Tallowmere Ledger</title>
<link rel="stylesheet" href="https://fonts.googleapis.com/css2?family=Poppins:wght@300;400;500;600&display=swap">
<style>
:root{
  --green:#3fa142;
  --green-dark:#2f8a33;
  --page:#f0f1f3;
  --ink:#2b2f33;
  --muted:#6b7075;
  --card:#ffffff;
  --footer:#22272a;
  --footer-line:#363c40;
  --footer-text:#c8ccce;
}
*{box-sizing:border-box;margin:0;padding:0}
html,body{width:705px;height:1200px;overflow:hidden}
body{position:relative;background:var(--page);font-family:'Poppins',sans-serif;color:var(--ink)}
.abs{position:absolute}

/* hero */
.hero{left:0;top:0;width:705px;height:240px}
.brand{left:92px;top:12px;display:flex;align-items:center;gap:8px;color:#fff;font-size:17px;font-weight:400;line-height:1.05;letter-spacing:.5px}
.brand-mark{width:14px;height:14px;background:var(--green)}
.main-nav{top:24px;left:380px;display:flex;gap:22px;font-size:6.6px;font-weight:500;letter-spacing:.5px;color:#fff}
.main-nav .current{color:var(--green)}
.page-title{top:96px;left:0;width:705px;text-align:center;color:#fff;font-weight:600;font-size:14px;letter-spacing:.3px}
.page-title .dash{display:block;font-size:8px;line-height:8px;font-weight:400;letter-spacing:1px}
.accent{color:var(--green)}

/* about card */
.about-card{left:92px;top:264px;width:521px;height:488px;background:var(--card);box-shadow:0 1px 4px rgba(0,0,0,.07)}
.about-photo{position:absolute;left:14px;top:14px;width:239px;height:188px;background:linear-gradient(160deg,#9fc6d9 0%,#d8e3ea 45%,#eef1f4 70%,#c5d3df 100%)}
.about-intro{position:absolute;left:270px;top:20px;width:236px}
.about-intro h1{font-size:14.5px;font-weight:500;margin-bottom:11px}
.body-text{font-size:6.6px;line-height:10.2px;color:var(--muted);font-weight:400}
.ticks{list-style:none;margin-top:13px}
.ticks li{font-size:6.6px;line-height:10.4px;color:var(--muted);display:flex;align-items:center;gap:6px}
.ticks svg{width:7px;height:7px}
.about-section{position:absolute;left:14px;width:492px}
.about-section h2{font-size:8.4px;font-weight:500;margin-bottom:9px;letter-spacing:.2px}
.about-section p+p{margin-top:10px}

/* contact */
.clouds{left:0;top:880px;width:705px;height:153px;background:linear-gradient(180deg,var(--page) 0%,#e3e6ea 30%,#c9ced4 60%,#eef0f2 85%,#dfe3e7 100%)}
.contact-head{top:788px;left:0;width:705px;text-align:center}
.contact-head small{display:block;font-size:5.6px;letter-spacing:.8px;color:var(--muted)}
.contact-head h2{font-size:12px;font-weight:500;letter-spacing:.3px}
.contact-head .dash{font-size:7px;line-height:6px;color:var(--muted);letter-spacing:1px}
.field{background:#fff;border:1px solid #e6e8ea;font-size:6.4px;color:var(--muted);padding:6px 7px}
.send{left:324px;top:929px;width:56px;height:19px;background:var(--green);color:#fff;font-size:6.4px;font-weight:500;display:flex;align-items:center;justify-content:center;gap:3px;letter-spacing:.4px;border:1px solid var(--green-dark)}

/* footer */
.site-footer{left:0;top:1033px;width:705px;height:167px;background:var(--footer);color:var(--footer-text)}
.footer-brand{position:absolute;left:92px;top:36px;display:flex;align-items:center;gap:7px;color:var(--green);font-size:13px;font-weight:500;line-height:1.15}
.footer-brand span.mark{width:12px;height:12px;background:var(--green);flex:none}
.footer-col h3{font-size:8.4px;font-weight:500;color:#fff;letter-spacing:.3px}
.footer-col p{font-size:7.6px;line-height:10.5px}
.footer-col .mail{text-decoration:underline}
.socials{display:flex;gap:7px;margin-top:10px}
.socials span{width:18px;height:18px;border:1px solid var(--green);border-radius:50%}
.socials span.on{background:var(--green)}
.badge{position:absolute;border-radius:50%}
.footer-rule{position:absolute;left:78px;top:118px;width:549px;height:1px;background:var(--footer-line)}
.copyright{position:absolute;left:92px;top:131px;font-size:7px}
.foot-nav{position:absolute;left:352px;top:132px;display:flex;gap:17px;font-size:6.4px;letter-spacing:.5px;font-weight:500}
.foot-nav .current{color:var(--green)}
.to-top{position:absolute;left:597px;top:128px}
</style>
</head>
<body>

<header class="hero abs">
  <svg width="705" height="240" viewBox="0 0 705 240" aria-hidden="true">
    <defs>
      <linearGradient id="deskTone" x1="0" y1="0" x2="1" y2="1">
        <stop offset="0" stop-color="#6a6b6c"/>
        <stop offset=".5" stop-color="#4c4d4e"/>
        <stop offset="1" stop-color="#5d5f61"/>
      </linearGradient>
    </defs>
    <polygon points="0,0 705,0 705,162 0,236" fill="url(#deskTone)" role="img" aria-label="Office desk with glasses and keyboard"/>
    <polygon points="0,76 248,210 705,162 705,175 0,236" fill="#3fa142"/>
  </svg>
  <div class="brand abs"><span class="brand-mark"></span>Tallowmere<br>Ledger</div>
  <nav class="main-nav abs">
    <span>HOME</span><span class="current">-- ABOUT US --</span><span>OUR SERVICES</span><span>CONTACT US</span>
  </nav>
  <h1 class="page-title abs"><span class="dash">------</span>ABOUT <span class="accent">US</span><span class="dash">------</span></h1>
</header>

<main>
  <section class="about-card abs">
    <div class="about-photo" role="img" aria-label="Business people meeting beside a desk with charts and a laptop"></div>
    <div class="about-intro">
      <h1>We Are Tallowmere Ledger</h1>
      <p class="body-text">Tallowmere Ledger originated with the idea of providing accounting services that would make clients feel safe and find refuge, feel confident that they could trust the numbers in their financial reports. The founders of Tallowmere Ledger migrated to Australia as refugees and the name of the business alludes to these origins. We strongly believe that every number counts..</p>
      <ul class="ticks">
        <li><svg viewBox="0 0 10 10"><path d="M1 5.5 4 8.5 9 2" stroke="#3fa142" stroke-width="2" fill="none"/></svg>Sed ut perspiciatis unde omnis</li>
        <li><svg viewBox="0 0 10 10"><path d="M1 5.5 4 8.5 9 2" stroke="#3fa142" stroke-width="2" fill="none"/></svg>Duis aute irure dolor in reprehenderit in voluptate</li>
        <li><svg viewBox="0 0 10 10"><path d="M1 5.5 4 8.5 9 2" stroke="#3fa142" stroke-width="2" fill="none"/></svg>Lorem ipsum dolor sit</li>
        <li><svg viewBox="0 0 10 10"><path d="M1 5.5 4 8.5 9 2" stroke="#3fa142" stroke-width="2" fill="none"/></svg>Excepteur sint occaecat cupidatat</li>
      </ul>
    </div>
    <div class="about-section" style="top:220px">
      <h2>Our Mission</h2>
      <p class="body-text">Lorem ipsum dolor sit amet, consectetur adipiscing elit, sed do eiusmod tempor incididunt ut labore et dolore magna aliqua. Ut enim ad minim veniam, quis nostrud exercitation ullamco laboris nisi ut aliquip ex ea commodo consequat. Duis aute irure dolor in reprehenderit in voluptate velit esse cillum dolore eu fugiat nulla pariatur. Excepteur sint occaecat cupidatat non proident, sunt in culpa qui officia deserunt mollit anim id est laborum.</p>
      <p class="body-text">Sed ut perspiciatis unde omnis iste natus error sit voluptatem accusantium doloremque laudantium, totam rem aperiam, eaque ipsa quae ab illo inventore veritatis et quasi architecto beatae vitae dicta sunt explicabo. Nemo enim ipsam voluptatem quia voluptas sit aspernatur aut odit aut fugit, sed quia consequuntur magni dolores eos qui ratione voluptatem sequi nesciunt.</p>
    </div>
    <div class="about-section" style="top:341px">
      <h2>Our Vision</h2>
      <p class="body-text">Lorem ipsum dolor sit amet, consectetur adipiscing elit, sed do eiusmod tempor incididunt ut labore et dolore magna aliqua. Ut enim ad minim veniam, quis nostrud exercitation ullamco laboris nisi ut aliquip ex ea commodo consequat. Duis aute irure dolor in reprehenderit in voluptate velit esse cillum dolore eu fugiat nulla pariatur. Excepteur sint occaecat cupidatat non proident, sunt in culpa qui officia deserunt mollit anim id est laborum.</p>
    </div>
    <div class="about-section" style="top:419px">
      <h2 style="margin-bottom:12px">Our Goal</h2>
      <p class="body-text">Sed ut perspiciatis unde omnis iste natus error sit voluptatem accusantium doloremque laudantium, totam rem aperiam, eaque ipsa quae ab illo inventore veritatis et quasi architecto beatae vitae dicta sunt explicabo. Nemo enim ipsam voluptatem quia voluptas sit aspernatur aut odit aut fugit, sed quia consequuntur magni dolores eos qui ratione voluptatem sequi nesciunt.</p>
    </div>
  </section>

  <div class="clouds abs" role="img" aria-label="Sky above a sea of clouds with distant snowy peaks"></div>

  <section class="contact-head abs">
    <small>NEEC HELP?</small>
    <h2>CONTACT <span class="accent">US</span></h2>
    <div class="dash">-----</div>
  </section>
  <div class="field abs" style="left:136px;top:836px;width:138px;height:20px">Name:</div>
  <div class="field abs" style="left:283px;top:836px;width:138px;height:20px">Email:</div>
  <div class="field abs" style="left:430px;top:836px;width:138px;height:20px">Phone:</div>
  <div class="field abs" style="left:136px;top:865px;width:432px;height:52px">Message...</div>
  <div class="send abs">
    <svg width="7" height="7" viewBox="0 0 10 10"><path d="M0 5 10 0 7 10 5 6Z" fill="#fff"/></svg>SEND
  </div>
</main>

<footer class="site-footer abs">
  <div class="footer-brand"><span class="mark"></span>Tallowmere<br>Ledger</div>
  <div class="footer-col abs" style="left:226px;top:29px">
    <h3>Call Us:</h3>
    <p>0400 - 118 - 562</p>
    <p class="mail">hello@tallowmereledger.com.au</p>
    <h3 style="margin-top:11px">Locations:</h3>
    <p>4410 Harbourview Rd,<br>Glenmore, NSW 2040</p>
  </div>
  <div class="footer-col abs" style="left:404px;top:29px">
    <h3>Get Social:</h3>
    <div class="socials"><span></span><span class="on"></span><span></span><span></span></div>
  </div>
  <span class="badge" style="left:553px;top:28px;width:29px;height:29px;background:#1ab4d7"></span>
  <span class="badge" style="left:584px;top:28px;width:29px;height:29px;background:#555a5e"></span>
  <span class="badge" style="left:553px;top:64px;width:38px;height:29px;border-radius:5px;background:#2d3236;border:1px solid #4a4f53"></span>
  <div class="footer-rule"></div>
  <p class="copyright">© 2017 Tallowmere Ledger. All rights reserved.</p>
  <nav class="foot-nav"><span>HOME</span><span class="current">-- ABOUT US --</span><span>OUR SERVICES</span><span>CONTACT US</span></nav>
  <svg class="to-top" width="16" height="14" viewBox="0 0 16 14" aria-label="Back to top"><path d="M8 0 16 14 8 9 0 14Z" fill="#3fa142"/></svg>
</footer>

</body>
</html>
```